Bright Meadow Patio In-Store Brochure

We sell bbq's, hot tubs, fireplaces, firepits... our company is at www.brightmeadowpatio-example.com . We would like the brochure to highlight some of our best brands (Tundra, HeatQuill, KRW, Vemba, DTN & Quenta grills / Orvik BBQ Equipment / Coastal Hearthwork Designs, Pellaro, Brindley, Waldemar fireplace / Tidewell Spas (Hot Tubs) / etc. see website!)

Target Market(s)

To give out to people when they come in to the store

Industry/Entity Type

It Company

Requirements
Must have
• An "About Us" section, show the manufacturers/brands that we deal with, have something about the 3 categories we sell to (BBQ/BBQ Equipment/ BBQ Islands.... Hot Tubs by Tidewell Spas..... Fireplaces / Firepits / Fireplace Media ).
Nice to have
• Website, phone, address, email, About Us, Brands that we deal with, etc.

```html
<!DOCTYPE html>
<html lang="en">
<head>
<meta charset="utf-8">
<title>Bright Meadow Patio – In-Store Brochure</title>
<link href="https://fonts.googleapis.com/css2?family=Source+Sans+3:ital,wght@0,400;0,600;1,600&family=Ubuntu:wght@500;700&family=Oswald:wght@300&display=swap" rel="stylesheet">
<style>
:root{
  --page:#d5d6d9;
  --paper:#ffffff;
  --paper-shade:#ecedee;
  --red:#c2161c;
  --red-dark:#8e0d12;
  --ink:#2a2a2a;
  --black:#1c1c1c;
  --bar-light:#e9e9e9;
}
*{box-sizing:border-box;margin:0;padding:0}
html,body{width:833px;height:1200px;overflow:hidden;background:var(--page)}
body{position:relative;font-family:"Source Sans 3",Arial,sans-serif;color:var(--ink)}
.sheet{position:absolute;left:89px;width:655px;height:510px;background:var(--paper);box-shadow:0 6px 10px rgba(0,0,0,.25);overflow:hidden}
.sheet--outside{top:91px}
.sheet--inside{top:637px}
.sheet svg.backdrop{position:absolute;left:0;top:0;width:655px;height:510px}
.abs{position:absolute}
.about-title{left:15px;top:120px;font-size:12px;color:var(--red);letter-spacing:.2px}
.body-copy{font-size:8.1px;line-height:9.75px;text-align:justify}
.about-copy{left:15px;top:137px;width:196px}
.bullets{list-style:none}
.bullets li{position:relative;padding-left:11px;font-size:8.1px;line-height:12.9px}
.bullets li::before{content:"";position:absolute;left:0;top:4px;width:5px;height:5px;border:1.4px solid var(--red);border-radius:50%}
.about-list{left:15px;top:226px;width:200px}
.about-sign{left:15px;top:344px;width:196px;text-align:center;font-size:7.8px;line-height:10.5px;color:var(--red);font-style:italic;font-weight:600}
.brand-name{font-family:"Source Sans 3",Arial,sans-serif;font-weight:600;color:var(--black);text-align:center;display:flex;align-items:center;justify-content:center;gap:6px}
.brand-name .mark{width:9px;height:9px;background:var(--black)}
.brand-mid{left:262px;top:132px;width:130px;font-size:14px;line-height:15px}
.brand-cover{left:465px;top:45px;width:160px;font-size:18px;line-height:19px}
.welcome{left:225px;top:230px;width:205px;text-align:center;font-family:"Ubuntu",sans-serif;font-weight:500;font-size:10.6px;line-height:15.3px;color:var(--red)}
.address{left:225px;top:437px;width:205px;text-align:center;color:#fff;font-size:9.2px;line-height:16px}
.cover-title{left:437px;top:412px;width:218px;text-align:center;font-family:"Oswald",sans-serif;font-weight:300;font-size:21px;line-height:25px;color:#fff;letter-spacing:.3px}
.bar{top:479px;height:20px;display:flex;align-items:center;justify-content:center;font-size:8.8px;letter-spacing:.6px}
.bar--estimate{left:0;width:221px;background:var(--black);color:#fff}
.bar--call{left:221px;width:216px;background:var(--bar-light);color:var(--black);letter-spacing:.4px}
.bar--web{left:437px;width:218px;background:var(--black);color:#fff;font-weight:600}
.cat-title{top:124px;height:34px;width:218px;display:flex;align-items:center;justify-content:center;color:#fff;font-family:"Ubuntu",sans-serif;font-weight:500;font-size:13.2px}
.col{top:185px;width:196px}
.col p{margin-bottom:9.75px}
.col .bullets li{line-height:12.9px}
.col--bbq{left:15px}.col--spa{left:231px}.col--fire{left:445px}
</style>
</head>
<body>

<section class="sheet sheet--outside" aria-label="Brochure outside panels">
  <svg class="backdrop" viewBox="0 0 655 510" aria-hidden="false">
    <defs>
      <linearGradient id="stone" x1="0" y1="0" x2="0" y2="1"><stop offset="0" stop-color="#2d2f2b"/><stop offset="1" stop-color="#6a6a63"/></linearGradient>
      <linearGradient id="redFill" x1="0" y1="0" x2="0" y2="1"><stop offset="0" stop-color="#d21d22"/><stop offset="1" stop-color="#9a0f14"/></linearGradient>
      <linearGradient id="flag" x1="0" y1="0" x2="1" y2="0"><stop offset="0" stop-color="#2b3a78"/><stop offset=".45" stop-color="#c9c9d2"/><stop offset="1" stop-color="#b3262b"/></linearGradient>
      <linearGradient id="patio" x1="0" y1="0" x2="0" y2="1"><stop offset="0" stop-color="#9a6a4a"/><stop offset=".5" stop-color="#8c8b86"/><stop offset="1" stop-color="#6d6660"/></linearGradient>
      <linearGradient id="paperFade" x1="0" y1="0" x2="1" y2="0"><stop offset="0" stop-color="#ffffff"/><stop offset="1" stop-color="#f0f0f0"/></linearGradient>
    </defs>
    <rect width="655" height="510" fill="url(#paperFade)"/>
    <g role="img" aria-label="Photo of a stone outdoor kitchen wall with mounted television">
      <path d="M0,0H440V76C320,64 150,72 0,128Z" fill="url(#stone)"/>
    </g>
    <path d="M0,128C150,72 320,64 440,76" fill="none" stroke="var(--red)" stroke-width="5"/>
    <path d="M0,138C150,82 320,72 440,84" fill="none" stroke="#d9d9d9" stroke-width="3"/>
    <g role="img" aria-label="Photo of a built-in stainless steel grill in a brick outdoor kitchen">
      <rect x="437" y="112" width="218" height="270" fill="url(#patio)"/>
    </g>
    <rect x="437" y="0" width="218" height="112" fill="#fff"/>
    <path d="M221,418C300,400 380,388 655,376V479H221Z" fill="url(#redFill)"/>
    <path d="M221,410C300,392 380,380 655,368" fill="none" stroke="#cfcfcf" stroke-width="3"/>
    <g role="img" aria-label="Illustration of an eagle over an American flag">
      <path d="M0,395C80,372 160,372 221,382V479H0Z" fill="url(#flag)"/>
    </g>
    <g role="img" aria-label="Map of the store location">
      <circle cx="327" cy="366" r="57" fill="#eef1ea" stroke="var(--red)" stroke-width="2"/>
    </g>
    <path d="M327,354c-4,0-6,3-6,6c0,5 6,11 6,11s6-6 6-11c0-3-2-6-6-6z" fill="var(--red)"/>
    <circle cx="327" cy="360" r="2" fill="#fff"/>
    <rect x="0" y="499" width="655" height="11" fill="url(#redFill)"/>
  </svg>

  <h2 class="abs about-title">ABOUT US</h2>
  <p class="abs body-copy about-copy">We ARE a direct-source for contractors, being able to build specialty products for most anything. We only sell quality - if you want price, then please go elsewhere. Again, it's important to note that we do not subscribe to the foreign-built junk grills, as they tend to be costly to repair and end up costing you more in the long run. Remember; it's your money - Why not get something good for it?</p>
  <ul class="abs bullets about-list">
    <li>Custom Designed BBQ Islands</li>
    <li>Entertainment Centers</li>
    <li>Hot Tubs made by Tidewell Spas</li>
    <li>Solvane Umbrella's that feature Auto-Tilt</li>
    <li>Most BBQ Grill manufacturers</li>
    <li>Custom Made stainless accessories</li>
    <li>Fireplaces, Logs, Firepits</li>
    <li>Delivery of most products to you by US</li>
  </ul>
  <p class="abs about-sign">So, come to Bright Meadow Patio..<br>we hope to make your cookin'... good lookin'!!</p>

  <div class="abs brand-name brand-mid"><span class="mark"></span><span>Bright Meadow Patio</span></div>
  <p class="abs welcome">We've been here since 2000,<br>helping our clients with<br>big &amp; small outdoor projects.<br>Let us help you, too!</p>
  <p class="abs address">1450 Meadowlark Lane,<br>Unit "D", Sunridge, CA, 90000</p>

  <div class="abs brand-name brand-cover"><span class="mark"></span><span>Bright Meadow Patio</span></div>
  <h1 class="abs cover-title">OUTDOOR<br>LIVING EXPERIENCE</h1>

  <div class="abs bar bar--estimate">FREE ESTIMATE</div>
  <div class="abs bar bar--call">Call Us Now: (555) 014-2277</div>
  <div class="abs bar bar--web">www.brightmeadowpatio-example.com</div>
</section>

<section class="sheet sheet--inside" aria-label="Brochure inside panels">
  <svg class="backdrop" viewBox="0 0 655 510">
    <defs>
      <linearGradient id="insidePaper" x1="0" y1="0" x2="1" y2="0"><stop offset="0" stop-color="#f1f1f1"/><stop offset=".33" stop-color="#fff"/><stop offset=".34" stop-color="#eee"/><stop offset=".66" stop-color="#fff"/><stop offset=".67" stop-color="#eee"/><stop offset="1" stop-color="#fff"/></linearGradient>
      <linearGradient id="titleBar" x1="0" y1="0" x2="0" y2="1"><stop offset="0" stop-color="#b3151a"/><stop offset="1" stop-color="#7f0c10"/></linearGradient>
      <linearGradient id="bottomRed" x1="0" y1="0" x2="0" y2="1"><stop offset="0" stop-color="#c8181e"/><stop offset="1" stop-color="#9b0f14"/></linearGradient>
      <linearGradient id="pBbq" x1="0" y1="0" x2="0" y2="1"><stop offset="0" stop-color="#4c4a3a"/><stop offset="1" stop-color="#8a7a66"/></linearGradient>
      <linearGradient id="pSpa" x1="0" y1="0" x2="0" y2="1"><stop offset="0" stop-color="#2a1f17"/><stop offset="1" stop-color="#6a5443"/></linearGradient>
      <linearGradient id="pFire" x1="0" y1="0" x2="0" y2="1"><stop offset="0" stop-color="#7b8a6a"/><stop offset="1" stop-color="#b8b6ac"/></linearGradient>
    </defs>
    <rect width="655" height="510" fill="url(#insidePaper)"/>
    <g role="img" aria-label="Photo of a stone BBQ island with flowers"><rect x="0" y="0" width="221" height="124" fill="url(#pBbq)"/></g>
    <g role="img" aria-label="Photo of a hot tub in a lit patio room"><rect x="221" y="0" width="216" height="124" fill="url(#pSpa)"/></g>
    <g role="img" aria-label="Photo of a firepit with chairs beside a pool"><rect x="437" y="0" width="218" height="124" fill="url(#pFire)"/></g>
    <rect x="0" y="124" width="655" height="34" fill="url(#titleBar)"/>
    <line x1="221" y1="0" x2="221" y2="158" stroke="#5a0a0d" stroke-width="1"/>
    <line x1="437" y1="0" x2="437" y2="158" stroke="#5a0a0d" stroke-width="1"/>
    <g fill="#fff">
      <rect x="14" y="396" width="96" height="52"/><rect x="116" y="396" width="96" height="52"/>
      <rect x="230" y="396" width="95" height="52"/><rect x="332" y="396" width="95" height="52"/>
      <rect x="444" y="396" width="95" height="52"/><rect x="546" y="396" width="95" height="52"/>
    </g>
    <g role="img" aria-label="Photos of built-in grill islands">
      <rect x="16" y="398" width="92" height="48" fill="#8a7d6a"/><rect x="118" y="398" width="92" height="48" fill="#6f6b60"/>
    </g>
    <g role="img" aria-label="Photos of hot tubs">
      <rect x="232" y="398" width="91" height="48" fill="#6f9db0"/><rect x="334" y="398" width="91" height="48" fill="#4a3a30"/>
    </g>
    <g role="img" aria-label="Photos of a firepit and an outdoor fireplace">
      <rect x="446" y="398" width="91" height="48" fill="#7a7a70"/><rect x="548" y="398" width="91" height="48" fill="#8d8a78"/>
    </g>
    <path d="M0,462C200,452 450,446 655,432" fill="none" stroke="#d3d3d3" stroke-width="4"/>
    <path d="M0,472C200,462 450,456 655,442V510H0Z" fill="url(#bottomRed)"/>
  </svg>

  <h2 class="abs cat-title" style="left:0">BBQ's and BBQ Islands</h2>
  <h2 class="abs cat-title" style="left:221px;width:216px">Hot Tubs (Spas)</h2>
  <h2 class="abs cat-title" style="left:437px">Fireplaces &amp; Firepits</h2>

  <div class="abs col col--bbq body-copy">
    <p>We carry various brands of residential and commercial quality BBQ grills. Grills like HeatQuill crest &amp; halo, or Tundra pro, use commercial-type burner systems made out of cast stainless. Brass (not red brass), as now used in the Pardo products, are susceptible to warping, and unlike stainless steel, takes a lot more time to cool off from a high temperature. Generally, overseas products are not the best in terms of quality manufacturing and quality control.</p>
    <p>We chose to carry grills that have given us excellent performance for many years. BBQ islands differ in quality and materials, and this degree varies from builder to builder. We are not a builder of bbq islands, but can supply you with a few people that do make quality products for your home.</p>
    <p>As we always say, let us save you some time and hard-earned money; buy quality, as it always costs less in the long run.</p>
  </div>

  <div class="abs col col--spa body-copy">
    <p>Open Air Living offers jet powered hot tubs from Aquarell Hot Tubs, the world's largest manufacturer of acrylic spas.</p>
    <p>Relax in you own back yard enjoying a comfortable and soothing jet powered therapeutic hydro-massage that will ease your muscle aches and relieve you of the stress of the day.</p>
    <p>The ongoing commitment to innovative product development ensures Aquarell's meets or exceeds your every need:</p>
    <ul class="bullets">
      <li>Energy efficient pumps produce high-performance</li>
      <li>Easy to program filtration and heating cycles</li>
      <li>Full foam insulation conserve energy</li>
      <li>Energy-saving immersion heating</li>
      <li>LED technology</li>
    </ul>
  </div>

  <div class="abs col col--fire body-copy">
    <p>Fireplaces and fire pits are an attractive way to add interest to your outdoor space. When the weather begins to cool off, these warming outdoor features can provide many benefits. Once built, you can enjoy it most of the year! What other outdoor feature offers so much?</p>
    <p>Sometimes, you have an idea in your head, or your designer has your idea in their head... :) And that means that no matter what, you can't just buy the product you want, but rather, you'll need to have it built for you.</p>
    <p>We offer customization services so that if you need an outdoor fireplace or firepit built, we can help! We'll get it built, have it delivered, hook it up to the gas line, and away you go!</p>
  </div>
</section>

</body>
</html>
```